Buss cards
Stationary & envelops
Buss cards - Transportation
Creative Brief
Simple
Harbor Crest Moving
412 West 57th Avenue Brooklyn, NY 11204
Info@Harborcrestmoving.example
www.harborcrestmoving.example
US DOT # 4718392
this is a moving company, that relocates household goods, any ideas you may have would be appreciated
Local & Long Distance Residential & Commercial Storage Facility visit us online: www.harborcrestmoving.example

```html
<!DOCTYPE html>
<html lang="en">
<head>
<meta charset="utf-8">
<title>Harbor Crest Moving — Business Card</title>
<link rel="stylesheet" href="https://fonts.googleapis.com/css2?family=Montserrat:wght@400;600;700;800&family=Open+Sans:wght@400;600&display=swap">
<style>
  :root {
    --stage: #3b3e43;
    --blue: #1f74c4;
    --blue-deep: #165fa8;
    --orange: #f39a1c;
    --white: #ffffff;
    --paper: #f4f5f6;
    --ink: #2c2f33;
    --muted: #6a6f75;
  }
  * { box-sizing: border-box; margin: 0; padding: 0; }
  html, body {
    width: 1200px; height: 797px; overflow: hidden;
    background: var(--stage);
  }
  .stage { position: relative; width: 1200px; height: 797px; }
  .card {
    position: absolute; top: 248px;
    width: 520px; height: 300px;
    border-radius: 18px; overflow: hidden;
    box-shadow: 0 10px 30px rgba(0,0,0,.35);
  }
  /* Front */
  .card--front {
    left: 50px;
    background: linear-gradient(135deg, var(--blue) 0%, var(--blue-deep) 100%);
    display: flex; flex-direction: column; align-items: center; justify-content: center;
    gap: 14px;
  }
  .brand {
    display: flex; align-items: center; gap: 10px;
    font-family: "Montserrat", sans-serif; font-weight: 800;
    color: var(--white); text-transform: uppercase; letter-spacing: .5px;
  }
  .brand__dot { width: 14px; height: 14px; border-radius: 50%; background: var(--orange); flex: none; }
  .card--front .brand { font-size: 28px; }
  .front__web {
    font-family: "Open Sans", sans-serif; font-size: 11px; color: var(--white); opacity: .9;
    letter-spacing: .4px;
  }
  /* Back */
  .card--back { left: 630px; background: var(--paper); }
  .card--back svg.back__shape { position: absolute; inset: 0; }
  .card--back .brand {
    position: absolute; left: 26px; top: 108px; font-size: 17px; width: 200px; line-height: 1.15;
  }
  .contact {
    position: absolute; left: 330px; top: 58px;
    list-style: none;
    font-family: "Open Sans", sans-serif; font-size: 10.5px; color: var(--ink);
    display: flex; flex-direction: column; gap: 6px;
  }
  .contact li { display: flex; align-items: flex-start; gap: 7px; line-height: 1.35; }
  .contact svg { width: 12px; height: 12px; flex: none; margin-top: 1px; }
  .person {
    position: absolute; left: 200px; top: 226px; width: 140px; text-align: center;
    font-family: "Open Sans", sans-serif;
  }
  .person__name { font-size: 15px; font-weight: 600; color: var(--ink); }
  .person__title { font-size: 10.5px; color: var(--muted); margin-top: 2px; }
</style>
</head>
<body>
<main class="stage">

  <section class="card card--front" aria-label="Card front">
    <div class="brand"><span class="brand__dot"></span>Harbor Crest Moving</div>
    <p class="front__web">www.harborcrestmoving.example</p>
  </section>

  <section class="card card--back" aria-label="Card back">
    <svg class="back__shape" viewBox="0 0 520 300" preserveAspectRatio="none" aria-hidden="true">
      <path d="M0 0 H290 C245 110 235 215 140 300 H0 Z" fill="var(--blue)"/>
      <path d="M296 0 C251 110 241 215 146 300" fill="none" stroke="var(--orange)" stroke-width="5"/>
    </svg>

    <div class="brand"><span class="brand__dot"></span>Harbor Crest Moving</div>

    <ul class="contact">
      <li>
        <svg viewBox="0 0 12 12"><path d="M6 1a3.5 3.5 0 0 0-3.5 3.5C2.5 7 6 11 6 11s3.5-4 3.5-6.5A3.5 3.5 0 0 0 6 1z" fill="var(--blue)"/><circle cx="6" cy="4.5" r="1.2" fill="#fff"/></svg>
        <span>412 West 57th Avenue<br>Brooklyn, NY 11204</span>
      </li>
      <li>
        <svg viewBox="0 0 12 12"><path d="M3 1.5l2 2-1 1.3a6 6 0 0 0 3.2 3.2l1.3-1 2 2-1.2 1.5C5.5 10.3 1.7 6.5 1.5 2.7z" fill="var(--blue)"/></svg>
        <span>718-555-0142</span>
      </li>
      <li>
        <svg viewBox="0 0 12 12"><rect x="1.5" y="4" width="9" height="5.5" rx="1" fill="var(--blue)"/><rect x="3.5" y="1.5" width="5" height="3" fill="var(--blue)"/></svg>
        <span>718-555-0143</span>
      </li>
      <li>
        <svg viewBox="0 0 12 12"><rect x="3.5" y="1" width="5" height="10" rx="1" fill="var(--blue)"/><circle cx="6" cy="9.5" r=".6" fill="#fff"/></svg>
        <span>718-555-0178</span>
      </li>
      <li>
        <svg viewBox="0 0 12 12"><rect x="1" y="2.5" width="10" height="7" rx="1" fill="var(--blue)"/><path d="M1.5 3l4.5 3.5L10.5 3" fill="none" stroke="#fff" stroke-width=".9"/></svg>
        <span>Info@Harborcrestmoving.example</span>
      </li>
      <li>
        <svg viewBox="0 0 12 12"><circle cx="6" cy="6" r="5" fill="var(--blue)"/><path d="M1 6h10M6 1c-2.5 3-2.5 7 0 10M6 1c2.5 3 2.5 7 0 10" fill="none" stroke="#fff" stroke-width=".7"/></svg>
        <span>www.harborcrestmoving.example</span>
      </li>
    </ul>

    <div class="person">
      <p class="person__name">Dana Whitlow</p>
      <p class="person__title">President</p>
    </div>
  </section>

</main>
</body>
</html>
```